New Website Design (Uncoded) Competition for Lorvex Trade Link

Please submit design concepts for a Joomla 3.0 Website for LORVEX TRADE LINK company. Our client prefers a modem style design, responsive to all mobile devices,
The website demo content needs to be clear and detailed.

Menu sample:
Home/About Us/Service/Strength/Partner/News/Contact US/Blog

Requirements:
1. Only need to submit the PSD for the design, coding work is not included.
2. Please submit both Homepage and Inner page to demonstrate the concept.
3. The Homepage needs to include: LOGO/MENU/Banner/Language Switcher/Company Introduction/Welcome module/Advertising Module/Footer Menu/Footer/Copyright/Social Links
4. Use Asian business women for demo pictures/Could try city pictures for background.
5. Prefer SINGLE SCREEN design rather than scrollable multiple screen designs.
6. Avoid any chain symbol since the company is more about financial business.
7. Avoid any direct connotations related with money or cash.
Updates

Hi Designers, I have clearly state the requirements that avoid using neg connontation pictures like cash/ property, though still receive concepts like that. Please check the brief clearly and mark at Update with "cheers" Kel from VT

Target Market(s)

Dongrui Lorvex Trade link Company provide cross-border Supply chain Financial service by integrating Dongrui Trade Link resource.
The Company mission is become the most respectful, professional and valuable Chinese Supply Chain Financial Company, pioneer the supply chain industry.

Industry/Entity Type

Financial

Font styles to use
Sans Serif

Colors
33b7a4

Requirements
Must have
• 1. Necessary Web element, including Logo/navigation/ Banner/ Footer
2. Asia business Women pictures.
Should not have
• 6. Avoid any chain symbol since the company is more about financial business.

```html
<!DOCTYPE html>
<html lang="en">
<head>
<meta charset="utf-8">
<title>Lorvex Trade Link</title>
<link href="https://fonts.googleapis.com/css2?family=Roboto:wght@400;500;700&family=Signika:wght@400&display=swap" rel="stylesheet">
<style>
:root{
  --teal:#33b7a4;
  --teal-dark:#23998a;
  --teal-text:#1f9987;
  --ink:#222;
  --grey:#5a5a5a;
  --footer:#333333;
  --footer-deep:#272727;
  --white:#ffffff;
}
*{margin:0;padding:0;box-sizing:border-box}
html,body{width:1200px;height:972px;overflow:hidden;background:var(--white);font-family:'Roboto',Arial,sans-serif;color:var(--ink)}
.page{position:relative;width:1200px;height:972px}
.site-header{position:absolute;left:0;top:0;width:1200px;height:96px;background:var(--white)}
.brand{position:absolute;left:200px;top:26px;display:flex;align-items:center;gap:10px}
.brand-dot{width:34px;height:34px;border-radius:50%;background:var(--teal)}
.brand-name{font-size:24px;font-weight:500;color:var(--grey);letter-spacing:1px;line-height:1}
.lang-select{position:absolute;left:818px;top:41px;width:182px;height:21px;border:1px solid #cfcfcf;font-size:11px;color:#555;padding:3px 6px}
.lang-select svg{position:absolute;right:7px;top:7px}
.main-nav{position:absolute;left:0;top:96px;width:1200px;height:37px;background:var(--teal)}
.nav-home{position:absolute;left:200px;top:0;width:37px;height:37px;background:var(--teal-dark);display:flex;align-items:center;justify-content:center}
.nav-list{position:absolute;left:237px;top:0;display:flex;list-style:none;height:37px}
.nav-list li{color:var(--white);font-size:12px;line-height:37px;padding:0 11px;position:relative}
.nav-list li::after{content:"";position:absolute;right:0;top:7px;height:23px;width:1px;background:rgba(255,255,255,.35)}
.nav-list li:first-child{padding-left:15px}
.search{position:absolute;left:819px;top:103px;width:181px;height:22px;background:var(--teal-dark);color:var(--white);font-size:10px;line-height:22px;padding-left:8px}
.search svg{position:absolute;right:6px;top:5px}
.hero{position:absolute;left:0;top:133px;width:1200px;height:588px;overflow:hidden;background:linear-gradient(90deg,#ffffff 0%,#ffffff 30%,#eef0ef 45%,#d9dddb 60%,#e6e8e7 100%)}
.hero-photo{position:absolute;left:480px;top:0;width:720px;height:588px;background:radial-gradient(ellipse at 62% 55%,#c8a894 0%,#6f5648 18%,#3a2c26 30%,rgba(230,232,231,0) 55%),linear-gradient(90deg,rgba(255,255,255,1) 0%,rgba(255,255,255,0) 35%);}
.hero-copy{position:absolute;left:200px;top:43px;width:400px}
.hero-tag{font-family:'Signika',sans-serif;font-size:23px;line-height:30px;color:var(--teal-text)}
.welcome{margin-top:38px;font-size:26px;font-weight:400;color:#111;white-space:nowrap}
.welcome b{font-weight:700;color:#444}
.welcome span{color:#555}
.intro{margin-top:12px;width:385px;font-size:11.7px;line-height:20px;color:#222}
.dots{display:flex;gap:4px;margin-top:16px}
.dots i{width:12px;height:12px;border-radius:50%;background:#a6d9d1}
.dots i.on{background:var(--teal-dark)}
.ad-band{position:absolute;left:0;top:721px;width:1200px;height:110px;background:var(--teal)}
.ad{position:absolute;left:297px;top:17px;width:607px;height:75px;background:var(--white);border:1px solid #d4d4d4;overflow:hidden}
.ad-scene{position:absolute;left:0;top:0;width:180px;height:75px;background:linear-gradient(180deg,#8fbfd9 0%,#5e8d5a 55%,#3d8fc0 80%,#2d7eb0 100%)}
.ad-title{position:absolute;left:232px;top:18px;font-size:26px;color:#666}
.ad-site{position:absolute;left:232px;top:50px;font-size:14px;color:#666}
.ad-big{position:absolute;left:395px;top:0;font-size:60px;font-weight:700;color:#f7a10a;line-height:75px;letter-spacing:-3px}
.ad-upto{position:absolute;left:466px;top:6px;font-size:14px;color:#555;line-height:16px}
.ad-pct{position:absolute;left:466px;top:22px;font-size:24px;color:#f7a10a;line-height:24px}
.ad-off{position:absolute;left:466px;top:46px;font-size:14px;color:#f7a10a}
.ad-btn{position:absolute;left:506px;top:25px;width:88px;height:24px;border-radius:12px;background:linear-gradient(#2fa5e6,#1577c4);color:var(--white);font-size:13px;font-weight:500;text-align:center;line-height:24px}
.site-footer{position:absolute;left:0;top:831px;width:1200px;height:111px;background:var(--footer)}
.foot-menu{position:absolute;top:13px;list-style:none}
.foot-menu li{color:var(--white);font-size:10.5px;line-height:24px}
.foot-menu.col-a{left:201px}
.foot-menu.col-b{left:306px;top:15px}
.foot-brand{position:absolute;right:200px;top:30px;display:flex;align-items:center;gap:10px}
.foot-brand .brand-name{color:var(--white)}
.foot-brand .brand-dot{background:var(--white)}
.copyright{position:absolute;left:0;top:942px;width:1200px;height:30px;background:var(--footer-deep);color:#aaa;font-size:9px;line-height:30px;padding-left:200px}
.social{position:absolute;right:200px;top:9px;display:flex;gap:10px}
.social i{width:13px;height:13px;border-radius:50%;background:var(--white)}
</style>
</head>
<body>
<div class="page">
  <header class="site-header">
    <div class="brand"><span class="brand-dot"></span><span class="brand-name">LORVEX TRADE LINK</span></div>
    <div class="lang-select">- - Select Language - -
      <svg width="10" height="6" viewBox="0 0 10 6"><path d="M0 0h10L5 6z" fill="#33b7a4"/></svg>
    </div>
  </header>
  <nav class="main-nav">
    <div class="nav-home">
      <svg width="18" height="16" viewBox="0 0 18 16"><path d="M9 1L1 8h2.5v7h4v-4.5h3V15h4V8H17z" fill="#fff"/></svg>
    </div>
    <ul class="nav-list">
      <li>About Us</li><li>Service</li><li>Strength</li><li>Partner</li><li>News</li><li>Contact us</li><li>Blog</li>
    </ul>
  </nav>
  <div class="search">Enter any keywords...
    <svg width="12" height="12" viewBox="0 0 12 12"><circle cx="5" cy="5" r="3.8" fill="none" stroke="#fff" stroke-width="1.5"/><path d="M8 8l3 3" stroke="#fff" stroke-width="1.6"/></svg>
  </div>
  <section class="hero">
    <div class="hero-photo" role="img" aria-label="Asian businesswoman in a white shirt smiling while on a phone call, soft office background"></div>
    <div class="hero-copy">
      <h2 class="hero-tag">Providing cross-border<br>Supply chain Financial service...</h2>
      <h1 class="welcome">Welcome to <b>LORVEX</b> <span>Trade Link</span></h1>
      <p class="intro">It is a long established fact that a reader will be distracted by the readable content of a page when looking at its layout. The point of using Lorem Ipsum is that it has a more-or-less normal distribution of letters, as opposed to using 'Content here, content here', making it look like readable English. Many desktop publishing packages and web page editors now use Lorem Ipsum as their default model text, and a search for 'lorem ipsum' will uncover many web sites still in their infancy. Various versions have evolved over the years, sometimes by accident, sometimes on purpose (injected humour and the like).</p>
      <div class="dots"><i></i><i class="on"></i><i></i><i></i></div>
    </div>
  </section>
  <section class="ad-band">
    <div class="ad">
      <div class="ad-scene" role="img" aria-label="Tropical island coastline travel scene with a Thailand sign"></div>
      <div class="ad-title">book hotels</div>
      <div class="ad-site">staylane.com</div>
      <div class="ad-big">75</div>
      <div class="ad-upto">up to</div>
      <div class="ad-pct">%</div>
      <div class="ad-off">off</div>
      <div class="ad-btn">book now!</div>
    </div>
  </section>
  <footer class="site-footer">
    <ul class="foot-menu col-a"><li>Home</li><li>About Us</li><li>Service</li><li>Strength</li></ul>
    <ul class="foot-menu col-b"><li>Partner</li><li>News</li><li>Contact us</li><li>Blog</li></ul>
    <div class="foot-brand"><span class="brand-dot"></span><span class="brand-name">LORVEX TRADE LINK</span></div>
  </footer>
  <div class="copyright">Copyright © 2014 Lorvex Trade Link. All Rights Reserved.
    <div class="social"><i aria-label="Social link"></i><i aria-label="Social link"></i><i aria-label="Social link"></i><i aria-label="Social link"></i></div>
  </div>
</div>
</body>
</html>
```